Larkfield Ecoworks Van Project

We would like to acquire a design for a brevo transit that utilizes our existing logo, our mascot design, and colors. I’m open to some changes, ideas, and adding of color to make it “pop.”
We would like to have our website, our phone number, and a small list of main services. We really want to accent the mascot, but I’m not sure how to blend it with our current logo. There may need to be a change to our logo to incorporate the mascot. I would like to add our logo to the mascots shirt and shovel, rather than the straight water droplet. If I need to have someone redesign the logo first, I will find someone to do that before the wrap if needed. We may be able to just replace the “house/roof” of the logo with the mascot in some way.

It looks as though it’s much too difficult with the file types to have the logo and mascot as one. So I would just like to utilize them separately if we need to. Message me to let me know what you need from me in order to have a real and professional wrap design. I’m open to extending the budget, as I had no idea what this kind of project costs when crowdsourcing.
Website is LarkfieldEcoworks.example
Phone is 555-214-7780

Target Market(s)

Home owners

Industry/Entity Type

Construction - Waterproofing

Font styles to use
Sans Serif

Colors
0054AA
0677BA
7BADD7
CADEEF
E8F1F8
0094D4
00A9DD
6FCCEA
C7EBF8
E9F6FB
F0912C
F2A743
F7CA91
FBE8D2
FDF5EE
6B429C
8869AF
B7A5CE
E3DAEB
F3F0F8

Requirements
Must have
• Please keep the beaver the same colors as he was originally. I don’t want a big baby blue beaver. If I need to find a way to export files differently, message me and I will fix it.
Nice to have
• We want our website, phone number, list of services. Ideally this will look like a legitimate truck wrap for a company.

```html
<!DOCTYPE html>
<html lang="en">
<head>
<meta charset="utf-8">
<title>Larkfield Ecoworks – Van Wrap Panels</title>
<link rel="stylesheet" href="https://fonts.googleapis.com/css2?family=Oswald:wght@500;700&display=swap">
<style>
  :root {
    --page: #c9dfea;
    --wrap-white: #ffffff;
    --bubble: #7badd7;
    --sky: #00a9dd;
    --sky-deep: #0094d4;
    --purple: #8869af;
    --ink: #0d0d0d;
  }
  html, body {
    margin: 0;
    width: 1200px;
    height: 675px;
    overflow: hidden;
    background: var(--page);
  }
  .wrap-panels { display: block; width: 1200px; height: 675px; }
  .service-list text {
    font-family: "Oswald", sans-serif;
    font-weight: 500;
    font-style: italic;
    font-size: 14px;
    fill: var(--ink);
  }
  .rear-services text {
    font-family: "Oswald", sans-serif;
    font-weight: 700;
    font-size: 16px;
    fill: var(--ink);
  }
  .brand-name {
    font-family: "Oswald", sans-serif;
    font-weight: 700;
    fill: var(--ink);
  }
  .web-address {
    font-family: "Oswald", sans-serif;
    font-weight: 700;
    fill: var(--wrap-white);
  }
  .phone-side {
    font-family: "Oswald", sans-serif;
    font-weight: 700;
    font-style: italic;
    font-size: 20px;
    fill: var(--wrap-white);
  }
  .phone-rear {
    font-family: "Oswald", sans-serif;
    font-weight: 700;
    font-size: 18px;
    fill: var(--ink);
  }
</style>
</head>
<body>
<svg class="wrap-panels" viewBox="0 0 1200 675" xmlns="http://www.w3.org/2000/svg">
  <defs>
    <clipPath id="side-clip"><rect x="30" y="150" width="740" height="370" rx="22"/></clipPath>
    <clipPath id="rear-clip"><rect x="800" y="150" width="370" height="370" rx="22"/></clipPath>
    <linearGradient id="mascot-tone" x1="0" y1="0" x2="0" y2="1">
      <stop offset="0" stop-color="#6b429c"/>
      <stop offset="0.25" stop-color="#9a6434"/>
      <stop offset="0.7" stop-color="#4a9fd8"/>
      <stop offset="1" stop-color="#8a5a30"/>
    </linearGradient>
  </defs>

  <!-- side panel -->
  <g class="side-panel">
    <rect x="30" y="150" width="740" height="370" rx="22" fill="var(--wrap-white)"/>
    <g clip-path="url(#side-clip)">
      <g fill="var(--bubble)" opacity="0.5">
        <circle cx="120" cy="470" r="90"/>
        <circle cx="330" cy="320" r="95"/>
        <circle cx="470" cy="410" r="85"/>
        <circle cx="660" cy="240" r="120"/>
      </g>
      <path d="M280 230 Q380 160 480 215" fill="none" stroke="var(--bubble)" stroke-width="3"/>
      <g fill="var(--bubble)">
        <circle cx="170" cy="400" r="4"/><circle cx="560" cy="360" r="4"/><circle cx="120" cy="270" r="4"/>
      </g>
      <path d="M30 470 L160 470 L185 446 L770 446 L770 464 L193 464 L168 488 L30 488 Z" fill="var(--purple)"/>
      <path d="M30 494 L175 494 L200 470 L770 470 L770 520 L30 520 Z" fill="var(--sky)"/>
      <rect x="30" y="508" width="740" height="12" fill="var(--sky-deep)"/>
    </g>

    <circle cx="62" cy="324" r="7" fill="var(--sky-deep)"/>
    <text class="brand-name" x="75" y="330" font-size="16">Larkfield Ecoworks</text>

    <rect x="200" y="165" width="130" height="165" rx="16" fill="url(#mascot-tone)"
          role="img" aria-label="Beaver mascot in purple hard hat holding a shovel, wearing a tool belt"/>

    <rect x="180" y="340" width="160" height="88" rx="6" fill="var(--wrap-white)" stroke="var(--ink)" stroke-width="4"/>
    <text class="brand-name" x="260" y="379" font-size="30" text-anchor="middle">LARKFIELD</text>
    <text class="brand-name" x="260" y="413" font-size="24" text-anchor="middle">ECOWORKS</text>

    <g class="service-list" text-anchor="end">
      <text x="565" y="185">FRENCH DRAINS</text>
      <text x="565" y="207">BURIED DOWNSPOUTS EXTENSIONS</text>
      <text x="565" y="229">YARD DRAINAGE</text>
      <text x="565" y="251">YARD DRAINS</text>
      <text x="565" y="273">RETAINING WALLS</text>
      <text x="565" y="295">GUTTER GUARDS</text>
      <text x="565" y="317">GUTTERS</text>
      <text x="565" y="339">DOWNSPOUTS</text>
    </g>

    <path d="M368 378 L598 378 L598 430 L350 430 Z" fill="var(--ink)"/>
    <text class="web-address" x="368" y="411" font-size="19">LarkfieldEcoworks.example</text>

    <rect x="605" y="160" width="155" height="350" rx="18" fill="url(#mascot-tone)"
          role="img" aria-label="Large beaver mascot in purple hard hat with shovel, flat tail and work boots"/>

    <text class="phone-side" x="60" y="510">555-214-7780</text>
  </g>

  <!-- rear panel -->
  <g class="rear-panel">
    <rect x="800" y="150" width="370" height="370" rx="22" fill="var(--wrap-white)"/>
    <g clip-path="url(#rear-clip)">
      <g fill="var(--bubble)" opacity="0.35">
        <circle cx="880" cy="230" r="110"/>
        <circle cx="1130" cy="480" r="100"/>
      </g>
    </g>
    <g class="rear-services" text-anchor="middle">
      <text x="985" y="195">FRENCH DRAINS</text>
      <text x="985" y="219">BURIED DOWNSPOUTS EXTENSIONS</text>
      <text x="985" y="243">YARD DRAINAGE</text>
      <text x="985" y="267">YARD DRAINS</text>
      <text x="985" y="291">RETAINING WALLS</text>
      <text x="985" y="315">GUTTER GUARDS</text>
      <text x="985" y="339">GUTTERS</text>
      <text x="985" y="363">DOWNSPOUTS</text>
    </g>
    <circle cx="921" cy="396" r="6" fill="var(--sky-deep)"/>
    <text class="brand-name" x="933" y="402" font-size="15">Larkfield Ecoworks</text>
    <path d="M870 420 L1150 420 L1150 452 L852 452 Z" fill="var(--ink)"/>
    <text class="web-address" x="1003" y="442" font-size="14" text-anchor="middle">LarkfieldEcoworks.example</text>
    <text class="phone-rear" x="1003" y="488" text-anchor="middle">555-214-7780</text>
  </g>
</svg>
</body>
</html>
```